Business Card Update, need to bring life to the card, two sided color

We need a new business card design, are moving and changing addresses and need a new look, we have the logos already attached but need a new style moving forward. Can incorporate the color of the logo (The Green) as well, maybe a solid back? We deal with safety products revolving around static electricity and safety lighting. Would like to keep same font in second logo as well.

Target Market(s)

Electrical Safety, Lighting

Contact Information for Business Card

Lars Whitcombe
Vice President
Office: 555-284-7316
Cell: 555-862-0457
lars@tkwhitcombe.com
www.tkwhitcombe.com
4700 West Cedar Boulevard
Suite #320
Roswell, GA 30412

Font styles to use
Serif
Sans Serif

Requirements
Must have
• Since 1918
Nice to have
• Could use the 100 Year Logo for back of card, would like the back of card to be the same green as logo.
Should not have
• No black cards please.

```html
<!DOCTYPE html>
<html lang="en">
<head>
<meta charset="utf-8">
<title>Business Card – Front and Back</title>
<link rel="stylesheet" href="https://fonts.googleapis.com/css2?family=Lato:wght@400;700&family=Arimo:wght@700&display=swap">
<style>
  :root {
    --backdrop: #4a4a4a;
    --brand-green: #03965a;
    --paper: #ffffff;
    --ink: #1c1c1c;
    --divider: #d4d4d4;
  }
  html, body {
    margin: 0;
    padding: 0;
    width: 1200px;
    height: 900px;
    overflow: hidden;
    background: var(--backdrop);
  }
  .canvas {
    position: relative;
    width: 1200px;
    height: 900px;
  }
  .card {
    position: absolute;
    width: 477px;
    height: 294px;
    box-shadow: 3px 4px 6px rgba(0,0,0,0.45);
    box-sizing: border-box;
  }
  .card-front {
    left: 120px;
    top: 275px;
    background: var(--paper);
    border-radius: 0 46px 0 46px;
  }
  .card-back {
    left: 606px;
    top: 273px;
    background: var(--brand-green);
    border-radius: 46px 0 46px 0;
  }

  /* front */
  .front-mark {
    position: absolute;
    left: 58px;
    top: 76px;
    width: 160px;
    text-align: center;
  }
  .front-mark-dot {
    display: block;
    width: 112px;
    height: 112px;
    margin: 0 auto 10px;
    border-radius: 50%;
    background: var(--brand-green);
  }
  .front-mark-name {
    font-family: "Arimo", Arial, sans-serif;
    font-weight: 700;
    font-size: 13px;
    color: var(--brand-green);
    white-space: nowrap;
  }
  .front-divider {
    position: absolute;
    left: 238px;
    top: 74px;
    width: 1px;
    height: 146px;
    background: var(--divider);
  }
  .contact {
    position: absolute;
    left: 262px;
    top: 67px;
    font-family: "Lato", Arial, sans-serif;
    color: var(--ink);
  }
  .contact-name {
    margin: 0;
    font-size: 22px;
    font-weight: 700;
    color: var(--brand-green);
    line-height: 24px;
  }
  .contact-title {
    margin: 0 0 3px;
    font-size: 13.5px;
    line-height: 16px;
  }
  .contact-list {
    list-style: none;
    margin: 0 0 5px;
    padding: 0;
  }
  .contact-list li {
    display: flex;
    align-items: center;
    font-size: 14px;
    line-height: 17.5px;
    white-space: nowrap;
  }
  .contact-icon {
    width: 10px;
    height: 10px;
    margin-right: 4px;
    fill: var(--brand-green);
    flex: none;
  }
  .contact-address {
    margin: 0;
    font-size: 14px;
    line-height: 17.5px;
    white-space: nowrap;
  }

  /* back */
  .back-mark {
    position: absolute;
    left: 88px;
    top: 108px;
    display: flex;
    align-items: center;
  }
  .back-mark-dot {
    width: 72px;
    height: 72px;
    border-radius: 50%;
    background: var(--paper);
    margin-right: 10px;
    flex: none;
  }
  .back-mark-text {
    font-family: "Arimo", Arial, sans-serif;
    font-weight: 700;
    color: var(--paper);
    white-space: nowrap;
  }
  .back-mark-name {
    display: block;
    font-size: 21px;
    line-height: 23px;
  }
  .back-mark-sub {
    display: block;
    font-size: 12.5px;
    line-height: 15px;
    padding-left: 14px;
  }
  .back-since {
    display: block;
    font-size: 11px;
    line-height: 15px;
    padding-left: 14px;
    letter-spacing: 0.5px;
  }
</style>
</head>
<body>
<main class="canvas">
  <section class="card card-front" aria-label="Card front">
    <div class="front-mark">
      <span class="front-mark-dot"></span>
      <span class="front-mark-name">Thomas K. Whitcombe</span>
    </div>
    <div class="front-divider"></div>
    <div class="contact">
      <h1 class="contact-name">Lars Whitcombe</h1>
      <p class="contact-title">Vice President</p>
      <ul class="contact-list">
        <li><svg class="contact-icon" viewBox="0 0 10 10"><path d="M0 3.5 Q5 0 10 3.5 L8.5 5 L7 4 L7 3 Q5 2.3 3 3 L3 4 L1.5 5 Z M2 6 L8 6 L9 9.5 L1 9.5 Z"/></svg>555-284-7316</li>
        <li><svg class="contact-icon" viewBox="0 0 10 10"><path d="M2.5 0 H7.5 A0.8 0.8 0 0 1 8.3 0.8 V9.2 A0.8 0.8 0 0 1 7.5 10 H2.5 A0.8 0.8 0 0 1 1.7 9.2 V0.8 A0.8 0.8 0 0 1 2.5 0 Z M3 1.2 V7.8 H7 V1.2 Z" fill-rule="evenodd"/></svg>555-862-0457</li>
        <li><svg class="contact-icon" viewBox="0 0 10 10"><path d="M0 2 H10 V8.5 H0 Z M0.8 2.6 L5 5.6 L9.2 2.6 V3.6 L5 6.6 L0.8 3.6 Z" fill-rule="evenodd"/></svg>lars@tkwhitcombe.com</li>
        <li><svg class="contact-icon" viewBox="0 0 10 10"><path d="M5 0 A5 5 0 1 1 5 10 A5 5 0 1 1 5 0 Z M4.3 1.2 Q2.2 2 2.6 3.6 L4 4.2 L3.6 6 L4.8 7.6 L5.2 8.8 Q7.6 8.2 8.6 6 L7 5.4 L6 3.6 L6.6 2.2 Z" fill-rule="evenodd"/></svg>www.tkwhitcombe.com</li>
      </ul>
      <p class="contact-address">4700 West Cedar Boulevard<br>Suite #320, Roswell, GA 30412</p>
    </div>
  </section>

  <section class="card card-back" aria-label="Card back">
    <div class="back-mark">
      <span class="back-mark-dot"></span>
      <span class="back-mark-text">
        <span class="back-mark-name">Thomas K. Whitcombe</span>
        <span class="back-mark-sub">Manufacturing Company, Inc.</span>
        <span class="back-since">Since 1918</span>
      </span>
    </div>
  </section>
</main>
</body>
</html>
```